New Infographic Design Project

I need a 1 page Infographic that explains our Velqor Strand offer.

Can you use the following content in the attached document to create a 1 page infographic. The image in the bottom of the document is one of our competitors who is offering the same thing, this image is only provided for inspiration and ideas as we need ours to be based on the content of the document and aligned with the Bruvell Brand

```html
<!DOCTYPE html>
<html lang="en">
<head>
<meta charset="utf-8">
<title>Data Ready. AI Ready. In 6 Weeks. | Bruvell</title>
<link href="https://fonts.googleapis.com/css2?family=Montserrat:wght@300;400;500;600;700;800&display=swap" rel="stylesheet">
<style>
:root{
  --navy:#0e1a4b;
  --red:#d2232f;
  --ink:#1b1f3a;
  --grey:#5d6072;
  --white:#ffffff;
}
*{margin:0;padding:0;box-sizing:border-box}
html,body{width:1200px;height:675px;overflow:hidden;background:var(--white)}
body{font-family:"Montserrat",sans-serif;color:var(--ink)}
.canvas{position:relative;width:1200px;height:675px;overflow:hidden;background:var(--white)}
.abs{position:absolute}

/* header */
.headline{left:36px;top:22px;font-weight:800;font-size:26px;line-height:30.5px;color:var(--navy);letter-spacing:-.3px}
.headline .dot{color:var(--red)}
.brace{left:228px;top:20px}
.intro-title{left:277px;top:18px;font-size:25px;font-weight:400;color:var(--navy);letter-spacing:-.2px}
.intro-text{left:280px;top:49px;width:725px;font-size:13px;line-height:15.7px;color:var(--ink)}
.intro-text .hl{color:var(--red)}
.brand{left:1030px;top:52px;width:140px;text-align:right}
.brand-name{font-size:24px;font-weight:700;color:var(--navy);letter-spacing:1.5px;line-height:28px}

/* main band */
.band{left:0;top:128px;width:1200px;height:547px;
  background:
    linear-gradient(180deg,rgba(255,255,255,0) 55%,rgba(255,255,255,.85) 100%),
    linear-gradient(100deg,#c5a1c0 0%,#a777aa 22%,#8664a1 45%,#4b5791 72%,#19407d 100%);}
.band-glow{left:0;top:128px;width:1200px;height:547px;
  background:radial-gradient(ellipse 420px 200px at 140px 500px,rgba(255,255,255,.9),rgba(255,255,255,0)),
             radial-gradient(ellipse 700px 160px at 600px 560px,rgba(255,255,255,.85),rgba(255,255,255,0))}
.edge-title{left:0;top:141px;width:1200px;text-align:center;color:var(--white);font-size:18px;font-weight:400;letter-spacing:15px}

.offer{left:1056px;top:148px;width:112px;height:27px;background:var(--white);border-radius:5px;padding:4px 0 0 7px;color:var(--navy)}
.offer small{display:block;font-size:6.3px;line-height:7px}
.offer span{display:block;font-size:8.6px;line-height:10px;font-weight:500}
.powered{left:1057px;top:184px;display:flex;align-items:center;gap:4px;color:var(--white)}
.powered small{font-size:6px;letter-spacing:.3px}
.powered i{display:block;width:16px;height:16px;background:var(--white)}
.powered b{font-size:10px;font-weight:600}

.pillar{color:var(--white)}
.pillar h3{font-size:16px;font-weight:300;line-height:19px}
.pillar p{font-size:11px;line-height:15.7px;font-weight:400}

/* six-week row */
.red-band{left:0;top:339px;width:1200px;height:142px;background:linear-gradient(90deg,#dc5c64 0%,#c9384f 40%,#c23a55 100%)}
.hero-six{left:30px;top:350px;color:var(--white)}
.hero-six .num{font-size:62px;font-weight:400;line-height:62px}
.hero-six .unit{font-size:31px;font-weight:500;line-height:26px;margin-top:-6px}
.hero-six .rule{width:90px;height:1.5px;background:var(--white);margin:7px 0 5px}
.hero-six .sub{font-size:12px;font-weight:500}
.timeline{left:0;top:434px;width:1200px;height:1.5px;background:var(--white)}
.node{width:7px;height:7px;border-radius:50%;background:var(--red);border:1.5px solid var(--white);top:431px}

.week-card{top:327px;width:162px;height:170px;background:linear-gradient(180deg,#e9eaf1 0%,#ffffff 40%);border-radius:9px;padding:19px 5px 0 12px}
.week-tag{position:absolute;left:13px;top:-6px;background:var(--red);color:var(--white);font-size:8px;font-weight:600;padding:2px 5px;border-radius:2px}
.week-card h4{font-size:10.2px;font-weight:600;color:var(--navy);line-height:11px;height:34px}
.week-card p{font-size:8.9px;line-height:15.6px;color:var(--grey)}

/* extra edge */
.extra{left:37px;top:533px;width:1123px;height:129px;border-radius:10px;background:linear-gradient(180deg,#e4e4ec 0%,#ffffff 55%)}
.bottom-red{left:0;top:642px;width:1200px;height:33px;background:var(--red)}
.extra-label{left:72px;top:580px;line-height:1}
.extra-label small{display:block;color:var(--red);font-size:12.5px;font-weight:400}
.extra-label span{display:block;color:var(--navy);font-size:25px;font-weight:300;margin-top:2px}
.perk h5{font-size:13.6px;font-weight:600;color:var(--navy);display:flex;align-items:center;gap:6px;white-space:nowrap}
.perk p{font-size:10px;line-height:15.7px;color:var(--grey);margin-top:19px}
.sep{top:560px;height:76px;border-left:1px dotted #8a8ca0}
</style>
</head>
<body>
<div class="canvas">

  <h1 class="abs headline">Data Ready<span class="dot">.</span><br>AI Ready<span class="dot">.</span><br>In 6 Weeks.</h1>
  <svg class="abs brace" width="16" height="96" viewBox="0 0 16 96" aria-hidden="true">
    <path d="M4 2 C10 2 10 8 10 16 V38 C10 44 12 46 15 48 C12 50 10 52 10 58 V80 C10 88 10 94 4 94" fill="none" stroke="var(--red)" stroke-width="2.2"/>
  </svg>
  <h2 class="abs intro-title">Your long-term strategic data partner</h2>
  <p class="abs intro-text">We start with a <span class="hl">Business Data Assessment</span> or <span class="hl">Strand Deployment Assessment</span> to pinpoint the highest-value use cases,the biggest data risks, and the fastest path to impact. We stand up a governed <span class="hl">Velqor Strand</span> foundation using&nbsp; repeatable ingestion, validation, and common data model patterns, so your reporting scales cleanly and your AI initiatives provide business value.</p>
  <div class="abs brand"><span class="brand-name">BRUVELL</span></div>

  <div class="abs band"></div>
  <div class="abs band-glow"></div>
  <div class="abs edge-title">THE BRUVELL EDGE</div>

  <div class="abs offer"><small>FULLY FUNDED FOR A</small><span>LIMITED TIME OFFER</span></div>
  <div class="abs powered"><small>POWERED BY</small><i></i><b>Northlake</b></div>

  <svg class="abs" style="left:0;top:0" width="1200" height="675" aria-hidden="true">
    <g fill="none" stroke="#fff" stroke-width="1" stroke-dasharray="3 3" opacity=".9">
      <path d="M158 190 V295 H356"/>
      <path d="M370 192 V306 H581"/>
      <path d="M600 192 V274 H864"/>
      <path d="M888 192 V291 H1032"/>
    </g>
    <g fill="none" stroke="#fff" stroke-width="1.3">
      <circle cx="158" cy="187" r="2.5"/><circle cx="370" cy="187" r="2.5"/>
      <circle cx="600" cy="187" r="2.5"/><circle cx="888" cy="187" r="2.5"/>
    </g>
    <circle cx="344" cy="194" r="9" fill="#fff"/>
    <path d="M339.5 194 l3 3 l5.5 -6" fill="none" stroke="var(--red)" stroke-width="2"/>
    <path d="M566 186 l8 4 v9 l-8 4 l-8 -4 v-9 z" fill="#fff"/>
    <path d="M566 194 l8 -4 v9 l-8 4 z" fill="var(--red)"/>
    <circle cx="857" cy="193" r="7.5" fill="none" stroke="#fff" stroke-width="1.8"/>
    <path d="M859 185 l-5 9 h4 l-3 8" fill="none" stroke="var(--red)" stroke-width="2"/>
    <circle cx="1013" cy="194" r="4.5" fill="none" stroke="#fff" stroke-width="2.4"/>
    <circle cx="1023" cy="194" r="4.5" fill="none" stroke="var(--red)" stroke-width="2.4"/>
  </svg>

  <div class="abs pillar" style="left:176px;top:185px;width:182px">
    <h3>Quality-first<br>delivery</h3>
    <p style="margin-top:21px">Automated validation, data tests, and “quality gates” that stop bad data upstream.</p>
  </div>
  <div class="abs pillar" style="left:390px;top:185px;width:192px">
    <h3>Data products,<br>not datasets</h3>
    <p style="margin-top:21px">Clear ownership, SLAs, versioning, and reusable, consumable outputs aligned to high impact business outcomes.</p>
  </div>
  <div class="abs pillar" style="left:617px;top:185px;width:230px">
    <h3>Governance that doesn’t<br>slow you down</h3>
    <p style="margin-top:18px">Security, access, lineage, and auditability built in from day one.</p>
  </div>
  <div class="abs pillar" style="left:904px;top:185px;width:140px">
    <h3>Operate<br>seamlessly</h3>
    <p style="margin-top:20px">CI/CD, monitoring, and cost controls so the platform stays healthy.</p>
  </div>

  <div class="abs red-band"></div>
  <div class="abs timeline"></div>
  <div class="abs hero-six">
    <div class="num">6</div>
    <div class="unit">week</div>
    <div class="rule"></div>
    <div class="sub">time to value</div>
  </div>

  <div class="abs week-card" style="left:120px"><span class="week-tag">WEEK 1</span>
    <h4>Envision &amp; Assess</h4>
    <p>Use case shortlist and priority based on highest business impact, current-state review, data risk &amp; compliance priorities, target operating model.</p></div>
  <div class="abs week-card" style="left:296px"><span class="week-tag">WEEK 2</span>
    <h4>Architecture &amp;<br>Governance Design</h4>
    <p>Landing zone decisions, security and access model, patterns/standards, delivery plan and success metrics.</p></div>
  <div class="abs week-card" style="left:473px"><span class="week-tag">WEEK 3</span>
    <h4>Strand Foundation<br>Deployed</h4>
    <p>Workspaces and environments, automation &amp; CI/CD, onboarding playbooks, baseline policies /guardrails.</p></div>
  <div class="abs week-card" style="left:650px"><span class="week-tag">WEEK 4</span>
    <h4>Data ingestion +<br>Validation Framework</h4>
    <p>Reusable ingestion patterns, automated validation, data contracts/SLAs, observability signals and alerting.</p></div>
  <div class="abs week-card" style="left:826px"><span class="week-tag">WEEK 5</span>
    <h4>Scalable Common<br>Data Model</h4>
    <p>Domain model, master entities, curated layer, semantic modelling patterns that support Lumetra Insight at scale.</p></div>
  <div class="abs week-card" style="left:1003px"><span class="week-tag">WEEK 6</span>
    <h4>Business outcomes +<br>AI-ready capability</h4>
    <p>Executive dashboards and priority reports, performance optimisation, hypercare and handover, AI readiness check and pilot plan (predictive analytics and/or secure enterprise LLM).</p></div>

  <span class="abs node" style="left:116px"></span>
  <span class="abs node" style="left:293px"></span>
  <span class="abs node" style="left:470px"></span>
  <span class="abs node" style="left:646px"></span>
  <span class="abs node" style="left:823px"></span>
  <span class="abs node" style="left:999px"></span>

  <div class="abs bottom-red"></div>
  <div class="abs extra"></div>
  <div class="abs extra-label"><small>EXTRA</small><span>EDGE</span></div>

  <div class="abs sep" style="left:396px"></div>
  <div class="abs sep" style="left:644px"></div>
  <div class="abs sep" style="left:904px"></div>

  <div class="abs perk" style="left:166px;top:557px;width:210px">
    <h5>“AI-ready data” guarantee <svg width="10" height="10" viewBox="0 0 10 10"><path d="M1 9 L9 1 M3 1 H9 V7" fill="none" stroke="var(--red)" stroke-width="1.5"/></svg></h5>
    <p>Every priority dataset ships with validation rules, ownership, lineage, and freshness SLAs before it can power AI.</p>
  </div>
  <div class="abs perk" style="left:420px;top:557px;width:182px">
    <h5>Cost-to-serve transparency <svg width="10" height="10" viewBox="0 0 10 10"><path d="M1 9 L9 1 M3 1 H9 V7" fill="none" stroke="var(--red)" stroke-width="1.5"/></svg></h5>
    <p>Show business owners what each product/report costs to run and optimise it continuously.</p>
  </div>
  <div class="abs perk" style="left:670px;top:557px;width:222px">
    <h5>Change-proof pipelines <svg width="10" height="10" viewBox="0 0 10 10"><path d="M1 9 L9 1 M3 1 H9 V7" fill="none" stroke="var(--red)" stroke-width="1.5"/></svg></h5>
    <p>Data contracts + automated tests reduce breakages from upstream schema changes.</p>
  </div>
  <div class="abs perk" style="left:928px;top:558px;width:205px">
    <h5>Governed self-serve <svg width="10" height="10" viewBox="0 0 10 10"><path d="M1 9 L9 1 M3 1 H9 V7" fill="none" stroke="var(--red)" stroke-width="1.5"/></svg></h5>
    <p>Catalog + certified datasets so teams move faster without creating data chaos.</p>
  </div>

</div>
</body>
</html>
```